Business Card Design

RETAIL HIGH END CONTEMPORARY WOMEN'S CLOTHING STORE
MODERN, SIMPLE, CLEAN, COOL

WE ARE ALL ABOUT NY and CALIF STYLE.... CLASSY but EDGY..
COOLEST DENIM , Trendsetting, NEUTRAL Pallettes,
Collections : Thread and Ivy, Corvin Dace, MPW, K47, GVD
Don't need names of collections on card. thats just good info
for designer of card.

WOULD LIKE THE FONT TO BE INTERESTING, but CLEAN
We are on facebook daily with photos of outfits we put together
which you can look up and friend us.... MellowDuneShop
Also on instagram .
Open to options on color and size, but need cool and fresh.

Industry/Entity Type

Business

Contact Information for Business Card

LORNA 5471 Harbor Ave. #318 Cedarline Court Shoppes..Va. Beach, Va. 23987
Phone 757.610.4825 Fax 757.610-3392 EMAIL..LORNABOUTIQUE@MAILVERO.COM

```html
<!DOCTYPE html>
<html lang="en">
<head>
<meta charset="utf-8">
<title>LORNA – Business Card</title>
<link rel="stylesheet" href="https://fonts.googleapis.com/css2?family=Jura:wght@300;400&family=Jost:wght@400;500&display=swap">
<style>
  :root {
    --page-bg: #e9e6e1;
    --card-bg: #134c62;
    --card-bg-soft: #175570;
    --text-light: #f2f6f7;
    --accent: #74c8c3;
    --accent-dark: #134c62;
    --icon: #7cc6c1;
  }
  html, body {
    margin: 0;
    width: 1200px;
    height: 887px;
    overflow: hidden;
    background: var(--page-bg);
  }
  .card {
    position: absolute;
    left: 271px;
    top: 236px;
    width: 658px;
    height: 415px;
    overflow: hidden;
    font-family: "Jost", "Futura", sans-serif;
    color: var(--text-light);
  }
  .card-texture {
    position: absolute;
    inset: 0;
    background: radial-gradient(circle at 50% 40%, var(--card-bg-soft), var(--card-bg) 75%);
  }
  .brand-name {
    position: absolute;
    left: 33px;
    top: 72px;
    margin: 0;
    font-family: "Jura", sans-serif;
    font-weight: 400;
    font-size: 62px;
    letter-spacing: 5px;
    line-height: 1;
    color: #ffffff;
  }
  .brand-tagline {
    position: absolute;
    left: 27px;
    top: 142px;
    margin: 0;
    font-size: 16px;
    letter-spacing: 1px;
  }
  .contact-list {
    position: absolute;
    left: 27px;
    top: 220px;
    margin: 0;
    padding: 0;
    list-style: none;
    font-size: 16.5px;
    letter-spacing: 0.6px;
  }
  .contact-item {
    position: relative;
    padding-left: 28px;
    line-height: 22px;
    margin-bottom: 11px;
  }
  .contact-icon {
    position: absolute;
    left: 0;
    top: 3px;
    width: 17px;
    height: 17px;
    fill: var(--icon);
  }
  .owner {
    position: absolute;
    left: 400px;
    width: 258px;
    top: 216px;
    text-align: center;
  }
  .owner-name {
    margin: 0;
    font-size: 22px;
    letter-spacing: 1px;
    line-height: 1.1;
  }
  .owner-title {
    margin: 0;
    font-size: 15px;
    color: var(--accent);
    letter-spacing: 0.5px;
  }
  .base-rule {
    position: absolute;
    left: 27px;
    top: 381px;
    width: 370px;
    height: 5px;
    background: var(--accent);
  }
  .social-tab {
    position: absolute;
    left: 390px;
    top: 342px;
    width: 268px;
    height: 46px;
    box-sizing: border-box;
    padding: 0 10px;
    background: var(--accent);
    color: var(--accent-dark);
    font-size: 14.5px;
    font-weight: 500;
    letter-spacing: 0.2px;
    white-space: nowrap;
    display: flex;
    align-items: center;
    justify-content: center;
  }
</style>
</head>
<body>
  <section class="card">
    <div class="card-texture" role="img" aria-label="Subtle tonal geometric pattern across the teal card background"></div>

    <h1 class="brand-name">LORNA</h1>
    <p class="brand-tagline">Womens Clothing Store</p>

    <ul class="contact-list">
      <li class="contact-item">
        <svg class="contact-icon" viewBox="0 0 24 24" aria-hidden="true"><path d="M7 2c1 0 1.6.6 2 1.6l1.2 3.2c.3.9 0 1.6-.7 2.1L8.3 9.8c.9 2.5 3 4.7 5.6 5.9l1-1.2c.6-.7 1.3-.9 2.1-.6l3.2 1.2c1 .4 1.6 1 1.6 2v2.4c0 1.5-1.2 2.5-2.7 2.4C10.5 21.3 2.7 13.5 2.1 4.8 2 3.2 3 2 4.6 2z"/></svg>
        757.610.4825
      </li>
      <li class="contact-item">
        <svg class="contact-icon" viewBox="0 0 24 24" aria-hidden="true"><rect x="2" y="8" width="6" height="14" rx="1"/><rect x="9" y="3" width="13" height="19" rx="1"/><rect x="11" y="5" width="9" height="5" fill="#134c62"/><rect x="11" y="13" width="3" height="2" fill="#134c62"/><rect x="16" y="13" width="3" height="2" fill="#134c62"/><rect x="11" y="17" width="3" height="2" fill="#134c62"/><rect x="16" y="17" width="3" height="2" fill="#134c62"/></svg>
        757.610-3392
      </li>
      <li class="contact-item">
        <svg class="contact-icon" viewBox="0 0 24 24" aria-hidden="true"><path d="M2 5h20v14H2z"/><path d="M2 5l10 8 10-8" fill="none" stroke="#134c62" stroke-width="1.6"/></svg>
        lornaboutique@mailvero.com
      </li>
      <li class="contact-item">
        <svg class="contact-icon" viewBox="0 0 24 24" aria-hidden="true"><path d="M12 1.5c-4 0-7 3-7 7 0 5 7 14 7 14s7-9 7-14c0-4-3-7-7-7zm0 10a3 3 0 1 1 0-6 3 3 0 0 1 0 6z"/></svg>
        5471 Harbor Ave. #318 Cedarline Court<br>Shoppes.Va. Beach, Va. 23987
      </li>
    </ul>

    <div class="owner">
      <p class="owner-name">Nyla.Veshkorn</p>
      <p class="owner-title">Owner</p>
    </div>

    <div class="base-rule"></div>
    <div class="social-tab">friendspage.com/MellowDuneShop</div>
  </section>
</body>
</html>
```